New Stationery Design Project

We got a project done from you for Pravonix stationary design. We have changed the name of the company from Pravonix to Kelmra.
So we want to redesign our stationay.
We are a VOIP, hosted pbx, and cloud services provider. Clients are mostly hotels, offices, business etc. needing phone services.
Our Slogan is : "Low cost, high quality service"
the logo has to be changed from Pravonix to Kelmra
Business address is
4172 Marrow Pkwy, suite 210
Dallas TX 75399
Phone: 555-013-4872
Fax: 555-013-4872
Website: Kelmra.example
Industry/Entity Type
Business
Look and feel
Each slider illustrates characteristics of the customer's brand and the style your logo design should communicate.

```html
<!DOCTYPE html>
<html lang="en">
<head>
<meta charset="utf-8">
<title>Kelmra Stationery</title>
<link rel="stylesheet" href="https://fonts.googleapis.com/css2?family=Alegreya+Sans:wght@700&family=Open+Sans:wght@700&display=swap">
<style>
  :root {
    --bg: #E6E7D3;
    --orange: #E98300;
    --cream: #FFFCD9;
    --paper: #FFFFFF;
    --ink-dark: #383C3F;
    --ink-navy: #1F4E6E;
    --motif-warm: rgba(255, 236, 90, 0.38);
    --motif-soft: rgba(214, 205, 168, 0.45);
    --shadow: 4px 6px 10px rgba(80, 80, 50, 0.28);
  }
  html, body {
    margin: 0;
    padding: 0;
    width: 1200px;
    height: 1000px;
    overflow: hidden;
    background: var(--bg);
  }
  .canvas {
    position: relative;
    width: 1200px;
    height: 1000px;
    background: var(--bg);
  }
  .sheet {
    position: absolute;
    box-shadow: var(--shadow);
    overflow: hidden;
  }
  .sheet--orange { background: var(--orange); }
  .sheet--white { background: var(--paper); }

  .envelope-front { left: 138px; top: 124px; width: 458px; height: 228px; }
  .envelope-back  { left: 138px; top: 388px; width: 458px; height: 230px; }
  .envelope-flap  { position: absolute; left: 0; top: 0; }

  .card-front { left: 676px; top: 91px; width: 187px; height: 104px; }
  .card-back  { left: 909px; top: 91px; width: 188px; height: 104px; }
  .letterhead { left: 662px; top: 249px; width: 438px; height: 620px; }

  /* Soft placeholder for the corner motif */
  .motif {
    position: absolute;
    right: 0;
    bottom: 0;
  }
  .motif--envelope {
    width: 280px;
    height: 180px;
    background: radial-gradient(ellipse at 60% 65%, var(--motif-warm) 0%, rgba(255, 236, 90, 0) 72%);
  }
  .motif--card {
    width: 102px;
    height: 67px;
    background: radial-gradient(ellipse at 60% 65%, var(--motif-warm) 0%, rgba(255, 236, 90, 0) 72%);
  }
  .motif--letterhead {
    width: 280px;
    height: 176px;
    background: radial-gradient(ellipse at 60% 65%, var(--motif-soft) 0%, rgba(214, 205, 168, 0) 72%);
  }

  .wordmark {
    position: absolute;
    display: flex;
    align-items: center;
    font-family: "Alegreya Sans", "Trebuchet MS", sans-serif;
    font-weight: 700;
    line-height: 1;
    white-space: nowrap;
  }
  .wordmark__dot {
    display: block;
    border-radius: 50%;
    background: currentColor;
  }

  .wordmark--envelope { left: 31px; top: 58px; font-size: 28px; color: var(--cream); gap: 6px; }
  .wordmark--envelope .wordmark__dot { width: 16px; height: 16px; }

  .wordmark--card-front { left: 104px; top: 52px; font-size: 12px; color: var(--cream); gap: 3px; }
  .wordmark--card-front .wordmark__dot { width: 7px; height: 7px; }

  .wordmark--card-back { left: 10px; top: 23px; font-size: 12px; color: var(--ink-navy); gap: 3px; }
  .wordmark--card-back .wordmark__dot { width: 7px; height: 7px; background: var(--orange); }

  .wordmark--letterhead { left: 27px; top: 51px; font-size: 23px; color: var(--ink-dark); gap: 5px; }
  .wordmark--letterhead .wordmark__dot { width: 12px; height: 12px; }

  .wordmark--colour { left: 60px; top: 860px; font-size: 64px; color: var(--ink-navy); gap: 10px; }
  .wordmark--colour .wordmark__dot { width: 36px; height: 36px; background: var(--orange); }

  .wordmark--mono { left: 322px; top: 860px; font-size: 64px; color: var(--ink-dark); gap: 10px; }
  .wordmark--mono .wordmark__dot { width: 36px; height: 36px; }

  .tagline {
    position: absolute;
    margin: 0;
    font-family: "Open Sans", Arial, sans-serif;
    font-weight: 700;
    font-size: 3.4px;
    line-height: 7px;
    letter-spacing: 0.1px;
    color: var(--ink-dark);
    text-transform: uppercase;
    white-space: nowrap;
  }
  .tagline--card { left: 11px; top: 86px; }
  .tagline--letterhead { left: 117px; top: 58px; }
</style>
</head>
<body>
<main class="canvas">

  <section class="sheet sheet--orange envelope-front" aria-label="Envelope front">
    <div class="wordmark wordmark--envelope"><span class="wordmark__dot"></span>Kelmra</div>
  </section>

  <section class="sheet sheet--orange envelope-back" aria-label="Envelope back">
    <svg class="envelope-flap" width="458" height="230" viewBox="0 0 458 230" aria-hidden="true">
      <polygon points="0,0 458,0 420,46 38,46" fill="var(--cream)"/>
    </svg>
    <div class="motif motif--envelope" role="img" aria-label="Cluster of outlined brand-motif shapes in pale yellow line art"></div>
  </section>

  <section class="sheet sheet--orange card-front" aria-label="Business card front">
    <div class="motif motif--card" role="img" aria-label="Cluster of outlined brand-motif shapes in pale yellow line art"></div>
    <div class="wordmark wordmark--card-front"><span class="wordmark__dot"></span>Kelmra</div>
  </section>

  <section class="sheet sheet--white card-back" aria-label="Business card back">
    <div class="wordmark wordmark--card-back"><span class="wordmark__dot"></span>Kelmra</div>
    <p class="tagline tagline--card">Low cost, high quality service · 555-013-4872<br>4172 Marrow Pkwy, suite 210, Dallas TX 75399</p>
  </section>

  <section class="sheet sheet--white letterhead" aria-label="Letterhead">
    <div class="wordmark wordmark--letterhead"><span class="wordmark__dot"></span>Kelmra</div>
    <p class="tagline tagline--letterhead">Low cost, high quality service · 555-013-4872<br>4172 Marrow Pkwy, suite 210, Dallas TX 75399</p>
    <div class="motif motif--letterhead" role="img" aria-label="Cluster of outlined brand-motif shapes in faint beige line art"></div>
  </section>

  <div class="wordmark wordmark--colour"><span class="wordmark__dot"></span>Kelmra</div>
  <div class="wordmark wordmark--mono"><span class="wordmark__dot"></span>Kelmra</div>

</main>
</body>
</html>
```